Website Design for Keystone Ridge Steelcraft And Decorative Forge LLC

Keystone Ridge Steelcraft & Decorative Forge is a veteran-owned and operated metal fabrication firm with decades of combined experience. We deliver custom, ornamental, and architectural metal solutions designed to meet the demands of commercial construction projects.

Our team specializes in fabricating and installing metal stairs, guardrails, handrails, railings, fencing, and ornamental metals that combined durability, code compliance, and visual appeal. We are a Small Business Enterprise (SBE), Veteran Business Enterprise (VBE), Service-Disabled Veteran-Owned Small Business (SDVOSB), and Veteran Friendly Business Enterprise (VFBE) Certified firm.

We are looking for a designer to create our website so that it can be used at our domain www.keystoneridgesteelcraftllc.example that we have sourced through Hostlark.example

We also have already created our corporate logo through crowdsource that can be incorporated into the web design.

Target Market(s)

General Contractors, Construction Managers, and Architects

Industry/Entity Type

Construction

Coding

Coded - Design and coding required

Number of Pages Required

5+ page

Requirements
Must have
• Company logo (Zip File Uploaded), About Us, Product Solutions, Target Market (See uploaded flyer)
Nice to have
• Patriotic Theme (American)
Should not have
• Web store

```html
<!DOCTYPE html>
<html lang="en">
<head>
<meta charset="utf-8">
<title>Keystone Ridge Steelcraft &amp; Decorative Forge</title>
<link href="https://fonts.googleapis.com/css2?family=Russo+One&family=Raleway:wght@400;500;600;700&display=swap" rel="stylesheet">
<style>
:root{
  --navy:#0f1f4b;
  --navy-deep:#0b1839;
  --red:#d71a3b;
  --red-dark:#b3122f;
  --ink:#1a1a1a;
  --muted:#6b6b6b;
  --light:#f3f3f3;
  --white:#ffffff;
}
*{box-sizing:border-box;margin:0;padding:0}
html,body{width:1200px;height:3408px;overflow:hidden}
body{font-family:"Raleway",sans-serif;color:var(--ink);background:var(--white);position:relative}
.abs{position:absolute}
.heading{font-family:"Russo One",sans-serif;font-weight:400;color:var(--ink);text-transform:uppercase}
.rule{height:4px;width:84px;background:var(--red)}
.btn{position:absolute;display:flex;align-items:center;justify-content:center;gap:8px;font-family:"Raleway",sans-serif;font-weight:700;text-transform:uppercase;border-radius:5px;color:var(--white);background:var(--red);font-size:14px;letter-spacing:.2px}
.btn svg{width:14px;height:14px}

/* top bar */
.topbar{top:0;left:0;width:1200px;height:32px;background:var(--navy)}
.topbar .contact{position:absolute;top:0;right:145px;height:32px;display:flex;align-items:center;gap:28px;color:var(--white);font-size:13px}
.topbar .contact span{display:flex;align-items:center;gap:7px}

/* nav */
.nav{top:32px;left:0;width:1200px;height:63px;background:var(--white);box-shadow:0 1px 4px rgba(0,0,0,.08)}
.brand{position:absolute;top:9px;left:145px;display:flex;align-items:center;gap:10px;z-index:3}
.brand-mark{width:46px;height:46px;border-radius:50%;background:var(--navy)}
.brand-name{font-family:"Raleway",sans-serif;font-weight:700;font-size:15px;line-height:1.15;color:var(--navy);width:150px}
.menu{position:absolute;right:145px;top:0;height:63px;display:flex;align-items:center;gap:40px;font-size:14px;font-weight:500;color:#222}
.menu .active{color:var(--red)}

/* hero */
.hero{top:95px;left:0;width:1200px;height:572px;background:radial-gradient(circle at 72% 55%,#6a8fb7 0%,#2f4260 18%,#232a33 45%,#14171c 80%)}
.hero h1{position:absolute;left:143px;top:134px;font-family:"Russo One",sans-serif;font-weight:400;color:var(--white);font-size:35px;line-height:60px;text-transform:uppercase;white-space:nowrap}
.hero .dots{position:absolute;left:144px;top:515px;display:flex;gap:10px}
.hero .dots i{display:block;width:24px;height:3px;background:var(--white)}
.hero .dots i.on{width:32px;background:var(--red)}

/* about */
.about-block{top:733px;left:112px;width:190px;height:229px;background:repeating-linear-gradient(-45deg,var(--navy) 0 5px,var(--white) 5px 10px)}
.about-photo{top:766px;left:144px;width:456px;height:439px;background:linear-gradient(135deg,#8a929a,#4d5660 55%,#2f3a3f)}
.flag{top:667px;left:979px;width:221px;height:246px;background:linear-gradient(160deg,#1e3170 0%,#3a4f8c 35%,#c62a3f 60%,#f2f2f2 78%,rgba(255,255,255,0) 100%);clip-path:polygon(20% 10%,100% 0,100% 100%,60% 80%,0 60%)}
.about h2{position:absolute;left:664px;top:800px;font-size:34px}
.about .rule{position:absolute;left:664px;top:852px}
.about p{position:absolute;left:666px;width:392px;font-size:13.6px;line-height:24px;color:#555}

/* industries */
.industries-bg{top:1277px;left:0;width:1200px;height:410px;background:var(--light)}
.industries-title{position:absolute;top:1337px;left:0;width:1200px;text-align:center;font-size:34px}
.industries-rule{top:1391px;left:558px}
.ind-card{position:absolute;top:1430px;width:300px;text-align:center}
.ind-icon{width:96px;height:96px;margin:0 auto;background:var(--navy);border-radius:4px;display:flex;align-items:center;justify-content:center}
.ind-card h3{margin-top:26px;font-size:18px;font-weight:500;color:#222}
.ind-card p{margin-top:8px;font-size:13.6px;line-height:24px;color:#666}
.arrow{position:absolute;top:1514px;width:18px;height:28px}

/* products */
.products-bg{top:1687px;left:0;width:1200px;height:597px;background:linear-gradient(180deg,#d71a3b,#c8183a)}
.products-title{position:absolute;top:1741px;left:0;width:1200px;text-align:center;font-size:34px;color:var(--white)}
.products-rule{top:1797px;left:552px;width:96px;background:var(--white)}
.products-lead{position:absolute;top:1826px;left:180px;width:840px;text-align:center;font-size:17px;line-height:29px;color:var(--white);font-weight:500}
.prod{position:absolute;top:1907px;width:216px;height:238px;background:var(--white)}
.prod .pic{width:216px;height:191px}
.prod span{display:block;text-align:center;line-height:47px;font-size:14px;color:#333}

/* why */
.why h2{position:absolute;top:2355px;left:0;width:1200px;text-align:center;font-size:34px}
.why-rule{top:2407px;left:558px}
.why-card{position:absolute;width:441px;height:127px;background:var(--white);box-shadow:0 0 10px rgba(0,0,0,.09)}
.why-card svg{position:absolute;left:20px;top:32px;width:62px;height:62px}
.why-card h3{position:absolute;left:106px;top:32px;font-size:17.5px;font-weight:500;color:#222}
.why-card p{position:absolute;left:107px;top:60px;width:310px;font-size:13.5px;line-height:23px;color:#777}

/* experiences */
.exp-bg{top:2883px;left:0;width:600px;height:374px;background:var(--light)}
.exp-photo{top:2883px;left:600px;width:600px;height:374px;background:linear-gradient(160deg,#c9d6e4 0%,#9fb3c9 40%,#7a8490 75%,#5b6169)}
.exp h2{position:absolute;left:145px;top:2936px;font-size:34px}
.exp .rule{position:absolute;left:145px;top:2988px}
.exp ul{position:absolute;left:145px;top:3025px;list-style:none}
.exp li{display:flex;align-items:center;gap:10px;font-size:13.5px;line-height:24px;color:#555}

/* footer */
.footer{top:3257px;left:0;width:1200px;height:151px;background:var(--navy)}
.footer nav{position:absolute;top:54px;left:0;width:1200px;display:flex;justify-content:center;gap:14px;color:var(--white);font-size:14px;font-weight:500}
.footer hr{position:absolute;top:100px;left:145px;width:910px;border:0;border-top:1px solid rgba(255,255,255,.45)}
.footer .copy{position:absolute;top:118px;left:0;width:1200px;text-align:center;color:var(--white);font-size:13.5px}
</style>
</head>
<body>

<div class="abs topbar">
  <div class="contact">
    <span><svg width="13" height="10" viewBox="0 0 13 10"><rect x="0" y="0" width="13" height="10" rx="1" fill="#fff"/><path d="M0 1l6.5 5L13 1" stroke="#0f1f4b" stroke-width="1.2" fill="none"/></svg>info@keystoneridgesteelcraftllc.example</span>
    <span><svg width="12" height="12" viewBox="0 0 24 24"><path fill="#fff" d="M6.6 10.8a15.1 15.1 0 006.6 6.6l2.2-2.2a1 1 0 011-.25 11.4 11.4 0 003.6.57 1 1 0 011 1V20a1 1 0 01-1 1A17 17 0 013 4a1 1 0 011-1h3.5a1 1 0 011 1c0 1.25.2 2.45.57 3.6a1 1 0 01-.25 1z"/></svg>(555) 014-2270</span>
  </div>
</div>

<header class="abs nav">
  <div class="brand"><div class="brand-mark"></div><div class="brand-name">Keystone Ridge Steelcraft</div></div>
  <nav class="menu">
    <span class="active">HOME</span><span>ABOUT US</span><span>PRODUCTS &#8964;</span><span>WHY CHOOSE US?</span><span>BLOG</span><span>CONTACT US</span>
  </nav>
</header>

<section class="abs hero" role="img" aria-label="Welder at work with a bright arc and flying sparks">
  <h1>Driven by mission.<br>Defined by integrity.<br>Built with quality.</h1>
  <div class="btn" style="left:144px;top:340px;width:175px;height:48px;font-size:15px">Get a Quote
    <svg viewBox="0 0 16 16"><circle cx="8" cy="8" r="8" fill="#fff"/><path d="M6.5 4.5L10 8l-3.5 3.5" stroke="#d71a3b" stroke-width="2" fill="none"/></svg></div>
  <div class="dots"><i class="on"></i><i></i><i></i></div>
</section>

<section class="about">
  <div class="abs about-block" aria-hidden="true"></div>
  <div class="abs about-photo" role="img" aria-label="Fabricator measuring steel pipework in a workshop"></div>
  <div class="abs flag" role="img" aria-label="Waving American flag"></div>
  <h2 class="heading">About Us</h2>
  <div class="rule"></div>
  <p style="top:882px">Keystone Ridge Steelcraft &amp; Decorative Forge LLC is a veteran owned and operated metal fabrication firm with decades of combined experience. We deliver custom, ornamental, and architectural metal solutions designed to meet the demands of commercial construction projects.</p>
  <p style="top:1010px">Our team specializes in fabricating and installing metal stairs, guardrails, handrails, railings, fencing, and ornamental metals that combine durability, code compliance.</p>
  <div class="btn" style="left:667px;top:1115px;width:144px;height:45px;font-size:13px">Read More
    <svg viewBox="0 0 16 16"><circle cx="8" cy="8" r="8" fill="#fff"/><path d="M6.5 4.5L10 8l-3.5 3.5" stroke="#d71a3b" stroke-width="2" fill="none"/></svg></div>
</section>

<section class="abs industries-bg"></section>
<h2 class="heading industries-title">Industrial We Serve</h2>
<div class="abs rule industries-rule"></div>
<svg class="arrow" style="left:62px" viewBox="0 0 18 28"><path d="M14 3L4 14l10 11" stroke="#222" stroke-width="3" fill="none"/></svg>
<svg class="arrow" style="left:1121px" viewBox="0 0 18 28"><path d="M4 3l10 11L4 25" stroke="#d71a3b" stroke-width="3" fill="none"/></svg>

<div class="ind-card" style="left:134px">
  <div class="ind-icon"><svg width="60" height="60" viewBox="0 0 60 60" fill="#fff"><rect x="14" y="10" width="4" height="42"/><rect x="4" y="12" width="42" height="4"/><rect x="40" y="16" width="2" height="12"/><rect x="28" y="28" width="24" height="24"/><rect x="31" y="32" width="5" height="5" fill="#0f1f4b"/><rect x="39" y="32" width="5" height="5" fill="#0f1f4b"/><rect x="31" y="41" width="5" height="5" fill="#0f1f4b"/><rect x="39" y="41" width="5" height="5" fill="#0f1f4b"/><rect x="4" y="52" width="52" height="3"/></svg></div>
  <h3>Commercial Construction</h3>
  <p>Lorem ipsum dolor sit amet, consectetur adipiscing elit, sed do eiusmod</p>
</div>
<div class="ind-card" style="left:452px">
  <div class="ind-icon"><svg width="60" height="60" viewBox="0 0 60 60" fill="#fff"><rect x="8" y="22" width="8" height="32"/><rect x="18" y="16" width="8" height="38"/><rect x="28" y="30" width="24" height="24"/><circle cx="46" cy="16" r="8"/><circle cx="46" cy="16" r="3" fill="#0f1f4b"/><rect x="32" y="36" width="6" height="6" fill="#0f1f4b"/></svg></div>
  <h3>Manufacturing Plants</h3>
  <p>Lorem ipsum dolor sit amet, consectetur adipiscing elit, sed do eiusmod</p>
</div>
<div class="ind-card" style="left:768px">
  <div class="ind-icon"><svg width="60" height="60" viewBox="0 0 60 60" fill="#fff"><rect x="8" y="8" width="5" height="26"/><rect x="16" y="18" width="10" height="14"/><rect x="29" y="18" width="10" height="14"/><rect x="42" y="18" width="10" height="14"/><rect x="6" y="33" width="48" height="4"/><circle cx="30" cy="46" r="9"/><circle cx="30" cy="46" r="3.5" fill="#0f1f4b"/></svg></div>
  <h3>Industrial Facilities</h3>
  <p>Lorem ipsum dolor sit amet, consectetur adipiscing elit, sed do eiusmod</p>
</div>

<section class="abs products-bg" aria-label="Our products"></section>
<h2 class="heading products-title">Our Products</h2>
<div class="abs rule products-rule"></div>
<p class="products-lead">We Provide A Full Range of Fabrication and Installation Services For Division 5 Metals and Division 32 Decorative Fences and Gates.</p>
<div class="prod" style="left:145px"><div class="pic" role="img" aria-label="Stainless steel handrail along a concrete stair" style="background:linear-gradient(160deg,#d9dcdf,#9da3a8)"></div><span>Handrails &amp; Guardrails</span></div>
<div class="prod" style="left:377px"><div class="pic" role="img" aria-label="Blue grated catwalk between yellow railings" style="background:linear-gradient(180deg,#c8b94a,#2c5f96 60%,#1b2f4c)"></div><span>Catwalks &amp; Platforms</span></div>
<div class="prod" style="left:608px"><div class="pic" role="img" aria-label="Spiral stairwell viewed from above" style="background:radial-gradient(circle,#1d1d1d 10%,#7a7a7a 50%,#bdbdbd)"></div><span>Custom Metal Fabrication</span></div>
<div class="prod" style="left:839px"><div class="pic" role="img" aria-label="Green painted metal stair railings" style="background:linear-gradient(160deg,#c8ccc8,#5f7a68 60%,#3b4a40)"></div><span>Decorative Metal Railings</span></div>
<div class="btn" style="left:524px;top:2183px;width:152px;height:44px;background:#fff;color:#d71a3b;font-size:13px">Learn More
  <svg viewBox="0 0 16 16"><circle cx="8" cy="8" r="8" fill="#d71a3b"/><path d="M6.5 4.5L10 8l-3.5 3.5" stroke="#fff" stroke-width="2" fill="none"/></svg></div>

<section class="why">
  <h2 class="heading">Why Contractors Choose Us?</h2>
  <div class="abs rule why-rule"></div>

  <div class="why-card" style="left:145px;top:2448px">
    <svg viewBox="0 0 62 62" fill="none" stroke="#0f1f4b" stroke-width="2.2"><rect x="5" y="10" width="40" height="36" rx="3"/><path d="M5 20h40M14 5v9M36 5v9M12 27h6M22 27h6M32 27h6M12 35h6M22 35h6"/><circle cx="46" cy="46" r="11" fill="#fff"/><path d="M46 39v7l5 3"/></svg>
    <h3>Stay On Schedule</h3>
    <p>We deliver projects on time, meeting even aggressive timelines</p>
  </div>
  <div class="why-card" style="left:615px;top:2448px">
    <svg viewBox="0 0 62 62" fill="none" stroke="#0f1f4b" stroke-width="2.2"><path d="M24 8h14l-4 8h-6z"/><path d="M28 16c-10 6-14 14-12 20 2 7 10 9 15 9s13-2 15-9c2-6-2-14-12-20"/><path d="M31 22v18M35 25c-2-2-8-2-8 2s8 2 8 6-6 4-8 2"/><path d="M4 44c6-2 10 2 16 4l14 2c4 1 4 5 0 5H20"/></svg>
    <h3>Lower Costs Over Time</h3>
    <p>Durable materials reduce maintenance and extend performance</p>
  </div>
  <div class="why-card" style="left:145px;top:2594px">
    <svg viewBox="0 0 62 62" fill="none" stroke="#0f1f4b" stroke-width="2.2"><circle cx="26" cy="26" r="14"/><path d="M26 4v6M26 42v6M4 26h6M42 26h6M10 10l4 4M38 38l4 4M42 10l-4 4M10 42l4-4"/><path d="M20 26l5 5 8-9"/><circle cx="42" cy="42" r="12" fill="#fff"/><circle cx="42" cy="42" r="7"/><circle cx="42" cy="42" r="2.5"/></svg>
    <h3>Get the Look You Wan</h3>
    <p>From functional handrails to custom ornamental features</p>
  </div>
  <div class="why-card" style="left:615px;top:2594px">
    <svg viewBox="0 0 62 62" fill="none" stroke="#0f1f4b" stroke-width="2.2"><path d="M24 8c6 0 14 4 14 10s-4 8-2 14 4 12-2 18c-4 4-6 0-6-4s-6-8-10-10-6-8-2-12"/><path d="M6 14l14 10M12 8l-8 8 4 4 8-8zM20 24l4-4"/></svg>
    <h3>American Made</h3>
    <p>Fabricated with pride in the USA, supporting local industries</p>
  </div>
  <div class="btn" style="left:524px;top:2760px;width:152px;height:42px;font-size:13px">Learn More
    <svg viewBox="0 0 16 16"><circle cx="8" cy="8" r="8" fill="#fff"/><path d="M6.5 4.5L10 8l-3.5 3.5" stroke="#d71a3b" stroke-width="2" fill="none"/></svg></div>
</section>

<section class="exp">
  <div class="abs exp-bg"></div>
  <div class="abs exp-photo" role="img" aria-label="Engineer in hard hat and safety vest inspecting a steel roof frame"></div>
  <h2 class="heading">Our Experiences</h2>
  <div class="rule"></div>
  <ul>
    <li><svg width="12" height="12" viewBox="0 0 12 12"><circle cx="6" cy="6" r="6" fill="#0f1f4b"/><path d="M3 6l2 2 4-4" stroke="#fff" stroke-width="1.6" fill="none"/></svg>Decades of combined fabrication experience</li>
    <li><svg width="12" height="12" viewBox="0 0 12 12"><circle cx="6" cy="6" r="6" fill="#0f1f4b"/><path d="M3 6l2 2 4-4" stroke="#fff" stroke-width="1.6" fill="none"/></svg>Proven track record with Fortune 500 manufacturers</li>
    <li><svg width="12" height="12" viewBox="0 0 12 12"><circle cx="6" cy="6" r="6" fill="#0f1f4b"/><path d="M3 6l2 2 4-4" stroke="#fff" stroke-width="1.6" fill="none"/></svg>Government, commercial, &amp; industrial project execution expertise</li>
    <li><svg width="12" height="12" viewBox="0 0 12 12"><circle cx="6" cy="6" r="6" fill="#0f1f4b"/><path d="M3 6l2 2 4-4" stroke="#fff" stroke-width="1.6" fill="none"/></svg>On-time, precision-built projects nationwide</li>
  </ul>
  <div class="btn" style="left:145px;top:3153px;width:152px;height:43px;font-size:13px">Learn More
    <svg viewBox="0 0 16 16"><circle cx="8" cy="8" r="8" fill="#fff"/><path d="M6.5 4.5L10 8l-3.5 3.5" stroke="#d71a3b" stroke-width="2" fill="none"/></svg></div>
</section>

<footer class="abs footer">
  <nav><span>HOME</span><span>|</span><span>ABOUT US</span><span>|</span><span>PRODUCTS</span><span>|</span><span>WHY CHOOSE US?</span><span>|</span><span>BLOG</span><span>|</span><span>CONTACT</span></nav>
  <hr>
  <div class="copy">Copyright © 2025 Keystone Ridge Steelcraft &amp; Decorative Forge</div>
</footer>

</body>
</html>
```